「働き方」をテーマにした本は、このところ多く出版されていますが、
著者がメイン読者(20~30代を中心としたビジネスパーソン)より上の世代だったり、
あるいは、充分なキャリアをお持ちの著者だったりするために、
読者自身が「自分事」として感じられないものが多いようです。
それに比べて本書の著者は30代半ばで、20代からパラレルキャリアを築き、
これからの新しい働き方を自ら模索・体現している方です(略歴は添付参照)。

そのため、より読者に近い目線の本であることを、カバーからも伝えたいです。

また、未来への不安を煽る内容ではなく、技術の進化や社会の変化によって、
これからの働き方やキャリアの築き方、ビジネスの始め方、さらには生き方にも
多くの可能性があり、現代はかつてないほどチャンスと希望に満ち溢れている時代だ、
と説いている点も、本書の特徴です。

そうした未来への明るい視点も感じられるデザインになるとうれしいです。
【仕様】
四六判(天地187ミリ×左右132ミリ、背幅12ミリ)・並製
カバー・帯・表紙・別丁扉
※詳細と原稿は添付ファイルをご参照ください。

●写真・イラスト等の素材を使うか否かを含めて、お任せいたします。
(有料素材となる場合は、その旨、明記してください)
●用紙銘柄や表面加工のご提案がありましたら、ぜひ明記してください。
デザインによっては、こちらから色違いのパターンをお願いする可能性もあります。
【弊社刊行書籍】
http://books.tsumugi-pub.co.jp/

【類書】
『ルート・ダイブ 迷いと焦りを手放す暮らし方の設計図〈2040〉』 マルタ・ヴェスリング(オルディナ社)
『まっさらな歩み方』 杉浦晴臣(コルネット社)
『明日の暮らしを描こう 道はいくつも、選べる』 ぽろめ(青嵐書房)

★ご提案いただいたデザインに対して、修正をお願いすることがあります。
★当選後に、文字修正を含めた最終調整を行った上で、入稿データを作成いただくことになります。
★本書の電子書籍版にも使用させていただきます。

何よりも、タイトル文字が大きく目立っている点が良かったです。
とくに、サブタイトルが見た人の目に飛び込んでくるところが、
他のデザイン案と比べたときに高評価につながりました。

また、せっかくこのような場でデザインを募集したので、
ふだんなら選ばない(あるいは提案されないような)デザインを選びたい、
という思いもありました。

書籍の装丁としての収まりの良さは備えつつも、
動きのある、印象的なデザインだと思います。ありがとうございます。

この度は、本当に多くの提案をいただき、誠にありがとうございます。
はじめての試みで、どんなデザインが上がってくるかドキドキしていましたが、
安定感のあるデザインから、とても斬新なデザインまで、幅広い案をいただき、
非常に頭を悩ませつつも、楽しい装丁選びとなりました。

またぜひ、こういった場で装丁デザインを募集したいと思いますので、
今後ともどうぞよろしくお願いいたします。

```html
<!DOCTYPE html>
<html lang="ja">
<head>
<meta charset="utf-8">
<title>ワーク・クラフト</title>
<link rel="stylesheet" href="https://fonts.googleapis.com/css2?family=Noto+Sans+JP:wght@400;500;700;900&display=swap">
<style>
  :root {
    --paper: #ffffff;
    --ink: #3a3a3a;
    --leaf: #9dc640;
    --leaf-pale: #e6f0cf;
    --leaf-soft: #b9d778;
    --on-leaf: #ffffff;
  }
  * { margin: 0; padding: 0; box-sizing: border-box; }
  html, body { width: 847px; height: 1200px; overflow: hidden; background: var(--paper); }
  .cover {
    position: relative;
    width: 847px;
    height: 1200px;
    background: var(--paper);
    font-family: "Noto Sans JP", sans-serif;
    color: var(--ink);
    overflow: hidden;
  }
  .leaf-band {
    position: absolute;
    left: 0; top: 585px;
    width: 847px; height: 615px;
    background: var(--leaf);
  }
  .art-upper {
    position: absolute;
    left: 415px; top: 215px;
    width: 185px; height: 345px;
    background: linear-gradient(160deg, var(--leaf-pale), #f6f6f6);
  }
  .art-lower {
    position: absolute;
    left: 200px; top: 585px;
    width: 350px; height: 180px;
    background: linear-gradient(180deg, var(--leaf-soft), var(--leaf));
  }
  .subtitle {
    position: absolute;
    left: 90px; top: 96px;
    font-size: 34px;
    font-weight: 500;
    letter-spacing: 0.5px;
    white-space: nowrap;
  }
  .author-role {
    position: absolute;
    left: 93px; top: 250px;
    font-size: 13px;
    font-weight: 500;
    line-height: 21px;
  }
  .author-name {
    position: absolute;
    left: 90px; top: 298px;
    font-size: 60px;
    font-weight: 500;
    letter-spacing: 4px;
    line-height: 1;
    white-space: nowrap;
  }
  .title {
    position: absolute;
    right: 56px; top: 40px;
    writing-mode: vertical-rl;
    font-size: 112px;
    font-weight: 900;
    line-height: 1;
    letter-spacing: -6px;
    color: var(--ink);
    white-space: nowrap;
  }
  .quote-open {
    position: absolute;
    left: 8px; top: 720px;
    font-size: 96px;
    font-weight: 700;
    line-height: 1;
    color: var(--on-leaf);
  }
  .blurb {
    position: absolute;
    left: 112px; top: 762px;
    font-size: 26px;
    font-weight: 700;
    line-height: 50px;
    letter-spacing: -0.5px;
    color: var(--on-leaf);
    white-space: nowrap;
  }
  .catch {
    position: absolute;
    left: 98px; top: 1010px;
    font-size: 76px;
    font-weight: 900;
    line-height: 1;
    letter-spacing: -1px;
    color: var(--on-leaf);
    white-space: nowrap;
  }
  .quote-close {
    position: absolute;
    left: 718px; top: 990px;
    font-size: 110px;
    font-weight: 700;
    line-height: 1;
    color: var(--on-leaf);
  }
  .publisher {
    position: absolute;
    left: 100px; top: 1136px;
    font-size: 26px;
    font-weight: 700;
    color: var(--on-leaf);
  }
</style>
</head>
<body>
  <main class="cover">
    <div class="leaf-band"></div>

    <div class="art-upper" role="img" aria-label="斜めに浮かぶ色付きの棒のイラスト"></div>
    <div class="art-lower" role="img" aria-label="緑の面から立ち上がる色付きの棒のイラスト"></div>

    <p class="subtitle">これからの『仕事の見取り図』</p>
    <p class="author-role">一般社団法人ソーシャル・ブリッジ代表理事<br>経営コンサルタント</p>
    <p class="author-name">長谷部周平</p>

    <h1 class="title">ワーク・クラフト</h1>

    <span class="quote-open">「</span>
    <p class="blurb">
      メイカーズ、クラウドソーシング、<br>
      クラウドファンディング、<br>
      ソーシャル・スタートアップ……<br>
      「仕事の未来」は、あらゆる可能性に満ちている。<br>
      あなたは、どの働き方を選びますか？
    </p>
    <p class="catch">働き方は無限大。</p>
    <span class="quote-close">」</span>

    <p class="publisher">つむぎパブリッシング</p>
  </main>
</body>
</html>
```